Letterhead Design

I would like 2 different letterheads. One with each logo I have attached. Business info:
Prairieline Medical Billing, LLC
4830 N Alder
Dunmore, KS 66923
(866) 555-0143

```html
<!DOCTYPE html>
<html lang="en">
<head>
<meta charset="utf-8">
<title>Prairieline Medical Billing – Letterhead</title>
<link rel="stylesheet" href="https://fonts.googleapis.com/css2?family=EB+Garamond:wght@400;500&family=Open+Sans:wght@400;700&display=swap">
<style>
  :root {
    --backdrop: #dcdcdc;
    --paper: #f7f7f8;
    --ink: #2b2b2b;
    --ink-soft: #555;
    --teal: #1597a5;
    --faint: #ececee;
  }
  * { margin: 0; padding: 0; box-sizing: border-box; }
  html, body { width: 1200px; height: 1091px; overflow: hidden; }
  body {
    background: var(--backdrop);
    display: flex; align-items: center; justify-content: center;
  }
  .letterhead {
    position: relative;
    width: 800px; height: 1035px;
    background: var(--paper);
    box-shadow: 0 2px 10px rgba(0,0,0,.12);
    overflow: hidden;
    font-family: "Open Sans", sans-serif;
    color: var(--ink);
  }
  .corner-arc { position: absolute; left: 0; bottom: 0; }
  .edge-band {
    position: absolute; left: 0; bottom: 0;
    width: 14px; height: 300px; background: var(--teal);
  }
  .brand {
    position: absolute; top: 48px; left: 210px;
    display: flex; align-items: center; gap: 12px;
  }
  .brand-mark { width: 22px; height: 22px; background: var(--teal); }
  .brand-name {
    font-weight: 700; font-size: 19px; color: var(--teal);
    letter-spacing: .2px;
  }
  .contact {
    position: absolute; top: 150px; right: 62px;
    text-align: right;
    font-family: "EB Garamond", serif; font-size: 18px; line-height: 1.6;
    color: var(--ink-soft);
  }
  .contact-accent {
    position: absolute; top: 150px; right: 40px;
    width: 4px; height: 88px; background: var(--teal);
  }
  .letter-body { position: absolute; top: 280px; left: 80px; width: 560px; }
  .subject { font-size: 10px; letter-spacing: .6px; color: var(--ink-soft); text-transform: uppercase; }
  .recipient { margin: 8px 0 22px 200px; font-family: "EB Garamond", serif; }
  .recipient-name { font-size: 22px; font-weight: 500; letter-spacing: .3px; }
  .recipient-role { font-size: 16px; }
  .paragraph {
    font-size: 13px; line-height: 1.55; text-align: justify;
    margin-bottom: 22px; color: var(--ink);
  }
  .signature {
    width: 150px; height: 60px; margin-top: 20px;
    background: var(--faint); border-radius: 4px;
  }
</style>
</head>
<body>
  <main class="letterhead">
    <svg class="corner-arc" width="420" height="420" viewBox="0 0 420 420" aria-hidden="true">
      <circle cx="70" cy="470" r="330" fill="#eeeef0"/>
    </svg>
    <div class="edge-band"></div>

    <header class="brand">
      <span class="brand-mark"></span>
      <span class="brand-name">Prairieline Medical Billing, LLC</span>
    </header>

    <address class="contact">
      Prairieline Medical Billing, LLC<br>
      4830 N Alder<br>
      Dunmore, KS 66923<br>
      (866) 555-0143
    </address>
    <div class="contact-accent"></div>

    <section class="letter-body">
      <p class="subject">Lorem ipsum dummy text</p>
      <div class="recipient">
        <p class="recipient-name">Mr. LOREM IPSUM</p>
        <p class="recipient-role">Designation, Company Name</p>
      </div>
      <p class="paragraph">Lorem Ipsum is simply dummy text of the printing and typesetting industry. Lorem Ipsum has been the industry's standard dummy text ever since the 1500s, when an unknown printer took a galley of type and scrambled it to make a type specimen book. It has survived not only five centuries, but also the leap into electronic typesetting, remaining essentially unchanged. It was popularised in the 1960s with the release of Lettermark sheets containing Lorem Ipsum passages, and more recently with desktop publishing software like Pagewright Studio including versions of Lorem Ipsum.</p>
      <p class="paragraph">Lorem Ipsum is simply dummy text of the printing and typesetting industry. Lorem Ipsum has been the industry's standard dummy text ever since the 1500s, when an unknown printer took a galley of type and scrambled it to make a type specimen book. It has survived not only five centuries, but also the leap into electronic typesetting, remaining essentially unchanged. It was popularised in the 1960s with the release of Lettermark sheets containing Lorem Ipsum passages, and more recently with desktop publishing software like Pagewright Studio including versions of Lorem Ipsum.</p>
      <p class="paragraph">Lorem Ipsum is simply dummy text of the printing and typesetting industry. Lorem Ipsum has been the industry's standard dummy text ever since the 1500s, when an unknown printer took a galley of type and scrambled it to make a type specimen book. It has survived not only five centuries, but also the leap into electronic typesetting, remaining essentially unchanged. It was popularised in the 1960s with the release of Lettermark sheets containing Lorem Ipsum passages, and more recently with desktop publishing software like Pagewright Studio including versions of Lorem Ipsum.</p>
      <div class="signature" role="img" aria-label="Handwritten signature"></div>
    </section>
  </main>
</body>
</html>
```